The Harbourlight CV consultant

The service is premium. It is aimed at people 18-30, so students and those looking to change their first job, principally in the UK but also global. It is offering a very personalised CV writing service and is much more expensive than others on offer. I am very keen that it should look simple and premium. It needs to look very professional, reflecting the aspirational jobs that the clients will be applying for.
If there were three words that summed it up: modern, clean, premium.
I am waiting for all the testimonials to come in but they need to form a major part of the website.
I am also waiting for the full logo design files so that I can upload them. In the meantime there is a copy of the logo.
Thoughts to help those yet to send a design...
This is a premium service and some of the designs have looked very generic. The focus needs to be on quality and the process mentioned in the brief. The partnership and the advantages it brings are crucial but few have mentioned that.

```html
<!DOCTYPE html>
<html lang="en">
<head>
<meta charset="utf-8">
<title>The Harbourlight CV consultant</title>
<link href="https://fonts.googleapis.com/css2?family=DM+Serif+Display&family=Roboto:wght@300;400;500;700&family=Poppins:wght@500&display=swap" rel="stylesheet">
<style>
:root{
  --blue:#1165bd;
  --blue-deep:#0e5aae;
  --cyan:#3cc6e8;
  --card-blue:#4a8fd2;
  --card-light:#f2eeec;
  --navy-text:#173a6e;
  --ink:#1b2a3a;
  --dark-panel:#25323f;
  --orange:#e0652a;
  --yellow:#f1c83a;
  --white:#ffffff;
  --muted:#e6eef8;
}
*{margin:0;padding:0;box-sizing:border-box}
html,body{width:1200px;height:4373px;overflow:hidden}
body{position:relative;font-family:'Roboto',sans-serif;color:var(--white);
  background:linear-gradient(180deg,#2fb6e6 82px,#1a86d2 420px,var(--blue) 760px,var(--blue) 100%);}
.abs{position:absolute}
.serif{font-family:'DM Serif Display',serif;font-weight:400}

/* header */
.site-header{left:0;top:0;width:1200px;height:82px;background:var(--white)}
.brand{left:88px;top:28px;color:var(--navy-text);font-family:'DM Serif Display',serif;font-size:24px;display:flex;align-items:center;gap:10px}
.brand-dot{width:12px;height:12px;border-radius:50%;background:var(--navy-text)}
.btn-outline{display:flex;align-items:center;justify-content:center;gap:8px;border:2px solid currentColor;border-radius:24px;font-size:14px;font-weight:500}
.header-btn{left:885px;top:20px;width:226px;height:42px;color:#1f6fc4}
.hero-btn{left:148px;top:583px;width:226px;height:43px;color:var(--white)}

.rule-line{left:69px;width:2px;background:rgba(255,255,255,.85)}

/* hero */
.hero-title{left:143px;top:170px;font-size:104px;line-height:112px;letter-spacing:-1px}
.hero-sub{left:155px;top:520px;font-size:23px;font-weight:300}
.cv-back{left:783px;top:143px;width:372px;height:440px;background:#4f5d6e;transform:rotate(3deg)}
.cv-back-inner{left:800px;top:160px;width:335px;height:410px;background:linear-gradient(160deg,#f4f6f9,#dfe6ef);transform:rotate(3deg)}
.cv-front{left:607px;top:275px;width:360px;height:430px;background:#a8dde8;transform:rotate(-4deg)}
.cv-front-inner{left:625px;top:290px;width:326px;height:400px;background:linear-gradient(170deg,#2c4560 0 9%,#f7f8fa 9%,#eef1f5 100%);transform:rotate(-4deg)}

/* question cards */
.q-card{top:800px;width:238px;height:268px;border-radius:50px;font-family:'DM Serif Display',serif;font-size:24px;line-height:34px;padding:48px 40px 0 48px}
.q-blue{background:var(--card-blue);color:var(--white)}
.q-light{background:var(--card-light);color:var(--ink)}

.invest{left:0;width:1200px;top:1152px;text-align:center;font-size:31px;font-weight:300;line-height:42px}
.name-mark{background:linear-gradient(transparent 58%,var(--orange) 58%,var(--orange) 88%,transparent 88%)}
.invest-copy{left:260px;width:680px;top:1256px;text-align:center;font-size:16.5px;line-height:25px;font-weight:300}

.people-title{left:113px;top:1460px;font-size:72px;line-height:77px}
.people-line{left:430px;top:1753px;width:198px;height:2px;background:var(--white)}
.people-copy{left:735px;top:1640px;width:340px;font-size:16.5px;line-height:26px;font-weight:300}

.hex-photo{left:10px;top:1845px;width:480px;height:445px}
.shake-circle{left:200px;top:2260px;width:236px;height:236px;border-radius:50%;background:var(--white);display:flex;align-items:center;justify-content:center}

.also-copy{left:545px;top:1890px;width:520px;font-size:15px;line-height:25px;font-weight:300}
.benefit{left:562px;font-family:'Poppins',sans-serif;font-weight:500;font-size:29px;display:flex;align-items:center;gap:14px}
.benefit .star{color:var(--yellow);font-size:38px;line-height:1;margin-top:10px}
.benefit-rule{left:538px;width:500px;height:2px;background:rgba(255,255,255,.8)}
.impress-copy{left:548px;top:2243px;width:450px;font-size:15.5px;line-height:25px;font-weight:300}

.partner-title{left:170px;top:2593px;font-size:46px}
.partner-sub{left:174px;top:2664px;font-size:29px;font-weight:300}
.partner-copy{left:180px;top:2718px;width:480px;font-size:15.5px;line-height:25px;font-weight:300}
.arch-photo{left:815px;top:2493px;width:318px;height:417px;border-radius:160px;background:radial-gradient(ellipse at 40% 40%,#f7e7c3,#d8ae6e 60%,#a87b45)}

/* band */
.band-photo{left:0;top:3010px;width:762px;height:412px;background:linear-gradient(120deg,#3a5a86,#2a4a75 50%,#6f8fb5)}
.band-panel{left:762px;top:3010px;width:438px;height:412px;background:var(--dark-panel);border-top-left-radius:24px}
.band-text{left:805px;top:3068px;width:330px;font-size:35px;line-height:49px}

/* process */
.process-title{left:135px;top:3565px;font-size:56px;line-height:62px}
.process-copy{left:130px;top:3720px;width:320px;font-size:17px;line-height:27px;font-weight:300}
.price{left:130px;top:3880px;font-size:21px;padding-bottom:8px;border-bottom:2px solid var(--white);width:360px}
.btn-dark{left:115px;top:4040px;width:212px;height:50px;border-radius:25px;background:#0b0f14;color:var(--white);font-size:14px;font-weight:500;display:flex;align-items:center;justify-content:center}
.step{background:rgba(20,70,150,.55);border:1.5px solid rgba(120,170,230,.55);border-radius:36px;padding:34px 28px 0 30px}
.step h3{font-size:17px;font-weight:500;line-height:21px;margin-bottom:16px}
.step p{font-size:14.5px;line-height:21px;font-weight:300;color:var(--muted)}
.step-num{position:absolute;left:34px;bottom:-4px;font-size:52px;font-weight:700;color:rgba(120,170,230,.35)}

.to-top{left:12px;top:4118px;width:43px;height:42px;background:#f0a21a;display:flex;align-items:center;justify-content:center}

/* footer */
.site-footer{left:0;top:4165px;width:1200px;height:208px;background:var(--white);color:var(--ink)}
.foot-connect{left:135px;top:4208px;font-size:22px;font-weight:700}
.foot-label{font-size:11px;font-weight:700;letter-spacing:.3px}
.foot-item{font-size:11px;color:#555}
.foot-rights{left:745px;top:4212px;font-size:12px;font-weight:500}
</style>
</head>
<body>

<header class="abs site-header"></header>
<div class="abs brand"><span class="brand-dot"></span>Harbourlight CV</div>
<a class="abs btn-outline header-btn">
  <svg width="13" height="13" viewBox="0 0 24 24"><path fill="currentColor" d="M6.6 10.8a15 15 0 0 0 6.6 6.6l2.2-2.2a1 1 0 0 1 1-.25 11.4 11.4 0 0 0 3.6.6 1 1 0 0 1 1 1V20a1 1 0 0 1-1 1A17 17 0 0 1 3 4a1 1 0 0 1 1-1h3.5a1 1 0 0 1 1 1c0 1.25.2 2.45.6 3.6a1 1 0 0 1-.25 1z"/></svg>
  Book an Introductory Call</a>

<div class="abs rule-line" style="top:82px;height:2928px"></div>
<div class="abs rule-line" style="top:3422px;height:743px"></div>

<h1 class="abs serif hero-title">Elevate<br>your CV’s<br>visibility..</h1>
<p class="abs hero-sub">Partner with a trusted CV writer.</p>
<a class="abs btn-outline hero-btn">
  <svg width="13" height="13" viewBox="0 0 24 24"><path fill="currentColor" d="M6.6 10.8a15 15 0 0 0 6.6 6.6l2.2-2.2a1 1 0 0 1 1-.25 11.4 11.4 0 0 0 3.6.6 1 1 0 0 1 1 1V20a1 1 0 0 1-1 1A17 17 0 0 1 3 4a1 1 0 0 1 1-1h3.5a1 1 0 0 1 1 1c0 1.25.2 2.45.6 3.6a1 1 0 0 1-.25 1z"/></svg>
  Book an Introductory Call</a>

<div class="abs cv-back"></div>
<div class="abs cv-back-inner" role="img" aria-label="Sample CV page with portrait and work history"></div>
<div class="abs cv-front"></div>
<div class="abs cv-front-inner" role="img" aria-label="Sample CV page with experience and skills columns"></div>

<div class="abs q-card q-blue" style="left:103px">Is your current CV not getting you results?</div>
<div class="abs q-card q-light" style="left:358px">Do you want to create a CV that stands out from the crowd?</div>
<div class="abs q-card q-blue" style="left:614px;padding-top:52px">Do you want to get a job more quickly?</div>
<div class="abs q-card q-light" style="left:873px">Do you want to earn more for the job your searching for?</div>

<p class="abs invest">If so then invest in a CV writing partnership<br>with <span class="name-mark">Daniel, the Harbourlight CV consultant.</span></p>
<p class="abs invest-copy">But first read the testimonials. These are real results from real people. They invested in thepartnership approach, and they’re delighted because it works. The blurb that follows is not as important as what they say &nbsp; I’d love it if you were the next person to appear in these testimonials. .</p>

<h2 class="abs serif people-title">People I work with<br>get a job sooner<br>and get a higher<br>paid job.</h2>
<div class="abs people-line"></div>
<p class="abs people-copy">Working with me is personalised, it’s a partnership. Together we will build a great CV that will present you in the best way possible, it will increase the chances of you securing the job you want.</p>

<svg class="abs hex-photo" viewBox="0 0 480 445" role="img" aria-label="Smiling candidate shaking hands at an interview">
  <defs><linearGradient id="hexfill" x1="0" y1="0" x2="1" y2="1"><stop offset="0" stop-color="#cfe0ee"/><stop offset=".6" stop-color="#8aa9c4"/><stop offset="1" stop-color="#e9eef3"/></linearGradient></defs>
  <path d="M240 8 Q258 0 276 8 L455 100 Q475 110 475 132 L475 320 Q475 342 455 352 L276 440 Q258 448 240 440 Q222 448 204 440 L25 352 Q5 342 5 320 L5 132 Q5 110 25 100 L204 8 Q222 0 240 8Z" fill="var(--orange)"/>
  <path d="M240 32 L440 132 L440 320 L240 420 L40 320 L40 132Z" fill="url(#hexfill)" stroke="#f3f3f3" stroke-width="8" stroke-linejoin="round"/>
</svg>
<div class="abs shake-circle">
  <svg width="140" height="90" viewBox="0 0 140 90" fill="none" stroke="#111" stroke-width="6" stroke-linejoin="round" stroke-linecap="round" aria-hidden="true">
    <path d="M6 28 L28 8 L44 26 L22 46Z"/><path d="M134 28 L112 8 L96 26 L118 46Z"/>
    <path d="M44 26 L60 18 L88 22 L96 26"/><path d="M22 46 L56 80 Q64 86 70 78 L108 50 L118 46"/>
    <path d="M62 22 L50 40 Q56 48 66 40 L78 30"/>
  </svg>
</div>

<p class="abs also-copy">And you’ll also get this. As a result of my approach everyone I’ve worked with is better prepared for interview. Our partnership will</p>
<div class="abs benefit" style="top:1980px"><span class="star">*</span>Increase self awareness</div>
<div class="abs benefit-rule" style="top:2040px"></div>
<div class="abs benefit" style="top:2068px"><span class="star">*</span>Improve presentation skills</div>
<div class="abs benefit-rule" style="top:2128px"></div>
<div class="abs benefit" style="top:2156px"><span class="star">*</span>Build the right sort of confidence</div>
<p class="abs impress-copy">And as a result you’ll impress at interview. You’ll develop a language and way of expressing yourself that shows the very best of you. And as that language sinks in and becomes part of you, you project a genuine confidence, quietly powerful, that recruiters will want in their teams.</p>

<h2 class="abs serif partner-title">The Partnership</h2>
<p class="abs partner-sub">The key to all this success is the partnership.</p>
<p class="abs partner-copy">Over four sessions we will, together, build a CV. You will get me, no one else, working with you for four sessions. There is a formula for success but it’s not formulaic.</p>
<div class="abs arch-photo" role="img" aria-label="Two people shaking hands in warm light"></div>

<div class="abs band-photo" role="img" aria-label="Person writing with a stylus on a tablet"></div>
<div class="abs band-panel"></div>
<p class="abs serif band-text">Your CV will be personal, you will shine through. Your CV will be elevated above the crowd.</p>

<h2 class="abs serif process-title">Our Resume<br>process is simple..</h2>
<p class="abs process-copy">I offer a premium service, very different to other offerings - so if like those in the testimonials, you get that job sooner, get a higher paid job, the investment is a wise one.</p>
<p class="abs serif price">Professionally Written Resume $149</p>
<a class="abs btn-dark">Get Started Today</a>

<div class="abs step" style="left:608px;top:3473px;width:235px;height:317px">
  <h3>Submit what<br>you have.</h3>
  <p>Got an existing resume? Send it. Just answer a few questions.once you do, we takes a deep-dive and goes to work on your resume.</p>
  <span class="step-num">01</span>
</div>
<div class="abs step" style="left:613px;top:3797px;width:230px;height:273px">
  <h3>Provide the details about you.</h3>
  <p>As we work on your resume, we sometimes have questions you need to answer.</p>
  <span class="step-num">02</span>
</div>
<div class="abs step" style="left:873px;top:3650px;width:237px;height:340px;padding-top:40px">
  <h3>Customize and<br>add on.</h3>
  <p>Extra great resume needs a little extra to help you stand out among the crowd of applicants.We also write cover letters, customize Profilia Profiles and offer personal career couseling.</p>
  <span class="step-num">03</span>
</div>

<div class="abs to-top"><svg width="16" height="12" viewBox="0 0 16 12" aria-hidden="true"><path d="M2 10 L8 4 L14 10" fill="none" stroke="#0e5aae" stroke-width="2.5"/></svg></div>

<footer class="abs site-footer"></footer>
<p class="abs foot-connect" style="color:var(--ink)">LET’S CONNECT</p>
<div class="abs" style="left:460px;top:4212px;color:var(--ink)">
  <p class="foot-label">CONTACT</p>
  <p class="foot-item" style="margin-top:4px">hello@harbourlightcv.co.uk</p>
  <p class="foot-label" style="margin-top:18px">GET IN TOUCH</p>
  <p class="foot-item" style="margin-top:6px">Profilia</p>
  <p class="foot-item" style="margin-top:6px">Folioshed</p>
  <p class="foot-item" style="margin-top:6px">Snapgrid</p>
</div>
<p class="abs foot-rights" style="color:var(--ink)">The Harbourlight CV Consultant - All Right Reserved</p>

</body>
</html>
```